Letterhead design x 2, follower page, with compliments slip and envelope design X 2

Design letterhead x 2, follower page, with compliments slip and envelope x 2 for Harbor Venture Partners, a business broking company. Using the colours of the existing logo and a white background for a clean, sophisticated look.

Target Market(s)

Family Business owners and regular business owners looking to buy or sell their business, or improve the value of their business.

Font styles to use
Sans Serif

Requirements
Must have
• Letterhead design 1 - Additional logos for Crale Business Sales, NTQR and DWL to be included in a small size somewhere on the page. Crale Business Sales logo only to have the wording 'Powered By' alongside. Please do not distort the size of the logos.
Letterhead design 2 - Additional logos for NTQR and DWL to be included in a small size somewhere on the page. This design will not include the Crale Business Sales logo or the words 'Powered By'. Please do not distort the size of the logos.
Envelope design 1 - Please include an address window
Envelope design 2 - Do not include an address window

```html
<!DOCTYPE html>
<html lang="en">
<head>
<meta charset="utf-8">
<title>Harbor Venture Partners – Stationery</title>
<link rel="stylesheet" href="https://fonts.googleapis.com/css2?family=Poppins:wght@300;400;500;600&display=swap">
<style>
:root{
  --orange:#f15a29;
  --grey:#9aa0a6;
  --grey-text:#7d8187;
  --grey-dark:#55595e;
  --rule-grey:#c9cccf;
  --navy:#1f2f6b;
  --ink:#222222;
  --paper:#ffffff;
  --backdrop:#dedede;
}
*{margin:0;padding:0;box-sizing:border-box}
html,body{width:1200px;height:1050px;overflow:hidden}
body{
  background:radial-gradient(ellipse at 50% 50%,#f1f1f1 0%,var(--backdrop) 70%);
  font-family:'Poppins',sans-serif;
  position:relative;
}
.sheet,.slip,.envelope{
  position:absolute;background:var(--paper);
  box-shadow:0 2px 6px rgba(0,0,0,.18);
}
.sheet{width:470px;height:664px;top:68px}
.sheet--first{left:104px}
.sheet--second{left:631px}

/* side bar */
.side-bar{position:absolute;left:0;top:0;width:12px;height:100%}
.side-bar span{position:absolute;left:0;width:12px}
.side-bar .seg-top{top:0;height:218px;background:var(--grey)}
.side-bar .seg-mid{top:220px;height:221px;background:var(--orange)}
.side-bar .seg-bottom{top:443px;bottom:0;background:var(--grey)}

/* brand lockup */
.brand{position:absolute;display:flex;align-items:center;gap:10px}
.brand-ring{width:46px;height:46px;border-radius:50%;border:3px solid var(--grey);flex:none}
.brand-name{color:var(--orange);font-weight:600;font-size:15px;line-height:14.5px;letter-spacing:-.2px}
.sheet .brand{left:33px;top:29px}

.contact{position:absolute;top:40px;font-size:7.6px;line-height:11.5px;color:var(--grey-dark);font-weight:400;white-space:nowrap}
.contact--address{left:282px}
.contact--phone{left:379px}
.contact-divider{position:absolute;left:369px;top:41px;width:1px;height:21px;background:var(--grey)}

.header-rules{position:absolute;left:34px;top:103px;width:403px;display:flex;gap:2px}
.header-rules span{flex:1;height:1px}
.header-rules .r-orange{background:var(--orange)}
.header-rules .r-grey{background:var(--rule-grey)}

.headline{position:absolute;left:32px;top:139px;font-size:25px;font-weight:300;color:var(--grey-text);letter-spacing:.3px}
.body-copy{position:absolute;left:33px;top:186px;width:404px;font-size:9px;line-height:12.6px;letter-spacing:.25px;color:var(--grey-text);text-align:justify;hyphens:auto}
.body-copy p{margin-bottom:25px}

.signature{position:absolute;left:376px;top:514px;width:38px;height:33px;background:linear-gradient(135deg,#eef0f7,#dfe3f0);border-radius:2px}
.signatory{position:absolute;right:34px;top:549px;text-align:right}
.signatory-name{font-size:11px;font-weight:600;color:var(--grey-text);line-height:14px}
.signatory-role{font-size:7px;color:var(--orange);line-height:10px}

.footer-bar{position:absolute;left:33px;top:629px;width:275px;height:12px;background:var(--orange);color:#fff;font-size:6.6px;line-height:12px;padding-left:6px;white-space:nowrap;overflow:hidden}
.badge{position:absolute;border-radius:50%}
.badge--seal{border:1.5px solid #8a96b8;background:#eef1f8}
.sheet .badge--seal{left:320px;top:626px;width:18px;height:18px}
.partner{position:absolute;display:flex;align-items:center;gap:5px}
.partner-dot{width:14px;height:14px;border-radius:50%;background:var(--navy);flex:none}
.partner-name{font-size:10px;font-weight:600;color:var(--navy);letter-spacing:1.5px}
.sheet .partner{left:355px;top:627px}

/* powered-by credit on letterhead 1 */
.sheet-credit{position:absolute;right:34px;top:606px;display:flex;align-items:baseline;gap:5px;white-space:nowrap}
.sheet-credit-label{font-size:6px;font-weight:500;color:var(--grey-text);letter-spacing:.6px;text-transform:uppercase}
.sheet-credit-name{font-size:8px;font-weight:600;color:var(--ink)}

/* compliments slip */
.slip{left:105px;top:772px;width:468px;height:210px}
.slip .brand{left:32px;top:27px}
.slip .brand-ring{width:48px;height:48px}
.slip .brand-name{font-size:16px;line-height:15.5px}
.stamp-box{position:absolute;left:401px;top:28px;width:39px;height:44px;border:1px solid #f0f0f0;color:#e2e2e2;font-size:6.5px;font-weight:500;text-align:center;line-height:42px}
.address-lines span{position:absolute;left:263px;width:177px;height:1px;background:#e6e6e6}
.base-band{position:absolute;left:0;bottom:0;width:100%;height:4px;background:var(--orange)}

/* envelope */
.envelope{left:634px;top:772px;width:466px;height:210px}
.flap-line{position:absolute;left:0;top:0}
.envelope .brand{left:170px;top:55px}
.envelope .brand-ring{width:48px;height:48px}
.envelope .brand-name{font-size:16px;line-height:15.5px}
.envelope-contact{position:absolute;left:0;top:112px;width:100%;text-align:center;font-size:7.8px;line-height:13px;color:var(--grey-text)}
.powered-by{position:absolute;left:166px;top:171px;font-size:5px;line-height:5.6px;color:var(--ink);font-weight:600;text-align:right;width:50px}
.envelope .badge--seal{left:220px;top:172px;width:14px;height:14px}
.envelope .partner{left:243px;top:173px;gap:3px}
.envelope .partner-dot{width:11px;height:11px}
.envelope .partner-name{font-size:7px;letter-spacing:1px}
</style>
</head>
<body>

<!-- Letterhead 1 -->
<section class="sheet sheet--first" aria-label="Letterhead, design one">
  <div class="side-bar"><span class="seg-top"></span><span class="seg-mid"></span><span class="seg-bottom"></span></div>
  <div class="brand"><div class="brand-ring"></div><div class="brand-name">Harbor<br>Venture<br>Partners</div></div>
  <div class="contact contact--address">2190 Marlow Rd NE #14<br>Ridgefield, AB T4R 2M6</div>
  <div class="contact-divider"></div>
  <div class="contact contact--phone">P: 403 555 0142<br>F: 403 555 0187</div>
  <div class="header-rules"><span class="r-orange"></span><span class="r-grey"></span><span class="r-orange"></span></div>
  <h1 class="headline">HEADLINE</h1>
  <div class="body-copy">
    <p>Lorem ipsum dolor sit amet, cetero accusamus intellegat at his, usu aeterno erroribus sadipscing id, nam virtute equidem reprimique ea. Est cu modo oblique theophrastus, vix ex ferri dicam iisque, idque nostrud eam ut. Tation constituto reprimique ut vis. Cu appareat dissentias qui. Vitae causae ceteros mea an, pro mutat admodum ex, ad quo commodo principes. Eam ignota impetus epicuri no, augue affert in vis. Pro nobis ver&shy;terem eu, ex ius alia utamur explicari.Lorem ipsum dolor sit amet, cetero accusamus in&shy;tellegat at his, usu aeterno erroribus sadipscing id, nam virtute equidem reprimique ea. Est cu modo oblique theophrastus, vix ex ferri dicam iisque, idque nostrud eam ut. Tation constituto reprimique ut vis. Cu appareat dissentias qui.</p>
    <p>Lorem ipsum dolor sit amet, cetero accusamus intellegat at his, usu aeterno erroribus sadipscing id, nam virtute equidem reprimique ea. Est cu modo oblique theophrastus, vix ex ferri dicam iisque, idque nostrud eam ut.</p>
    <p>Tation constituto reprimique ut vis. Cu appareat dissentias qui. Vitae causae ceteros mea an, pro mutat admodum ex, ad quo commodo principes. Eam ignota impetus epi&shy;curi no, augue affert in vis. Pro nobis verterem eu, ex ius alia utamur explicari.Lorem ipsum dolor sit amet, cetero accusamus intellegat at his, usu aeterno erroribus sadip&shy;scing id, nam virtute equidem reprimique ea. Est cu modo oblique theophrastus, vix ex ferri dicam iisque, idque nostrud eam ut. Tation constituto reprimique ut vis. Cu appar&shy;eat dissentias qui.</p>
  </div>
  <div class="signature" role="img" aria-label="Handwritten signature"></div>
  <div class="signatory"><div class="signatory-name">Daniel Hargreave</div><div class="signatory-role">Product Director</div></div>
  <div class="sheet-credit"><span class="sheet-credit-label">Powered by</span><span class="sheet-credit-name">Crale Business Sales</span></div>
  <div class="footer-bar">info@harborventurepartners.com.au &nbsp;|&nbsp; www.harborventurepartners.com.au</div>
  <div class="badge badge--seal" role="img" aria-label="DWL membership badge"></div>
  <div class="partner"><span class="partner-dot"></span><span class="partner-name">NTQR</span></div>
</section>

<!-- Letterhead 2 -->
<section class="sheet sheet--second" aria-label="Letterhead, design two">
  <div class="side-bar"><span class="seg-top"></span><span class="seg-mid"></span><span class="seg-bottom"></span></div>
  <div class="brand"><div class="brand-ring"></div><div class="brand-name">Harbor<br>Venture<br>Partners</div></div>
  <div class="contact contact--address">2190 Marlow Rd NE #14<br>Ridgefield, AB T4R 2M6</div>
  <div class="contact-divider"></div>
  <div class="contact contact--phone">P: 403 555 0142<br>F: 403 555 0187</div>
  <div class="header-rules"><span class="r-orange"></span><span class="r-grey"></span><span class="r-orange"></span></div>
  <h1 class="headline">HEADLINE</h1>
  <div class="body-copy">
    <p>Lorem ipsum dolor sit amet, cetero accusamus intellegat at his, usu aeterno erroribus sadipscing id, nam virtute equidem reprimique ea. Est cu modo oblique theophrastus, vix ex ferri dicam iisque, idque nostrud eam ut. Tation constituto reprimique ut vis. Cu appareat dissentias qui. Vitae causae ceteros mea an, pro mutat admodum ex, ad quo commodo principes. Eam ignota impetus epicuri no, augue affert in vis. Pro nobis ver&shy;terem eu, ex ius alia utamur explicari.Lorem ipsum dolor sit amet, cetero accusamus in&shy;tellegat at his, usu aeterno erroribus sadipscing id, nam virtute equidem reprimique ea. Est cu modo oblique theophrastus, vix ex ferri dicam iisque, idque nostrud eam ut. Tation constituto reprimique ut vis. Cu appareat dissentias qui.</p>
    <p>Lorem ipsum dolor sit amet, cetero accusamus intellegat at his, usu aeterno erroribus sadipscing id, nam virtute equidem reprimique ea. Est cu modo oblique theophrastus, vix ex ferri dicam iisque, idque nostrud eam ut.</p>
    <p>Tation constituto reprimique ut vis. Cu appareat dissentias qui. Vitae causae ceteros mea an, pro mutat admodum ex, ad quo commodo principes. Eam ignota impetus epi&shy;curi no, augue affert in vis. Pro nobis verterem eu, ex ius alia utamur explicari.Lorem ipsum dolor sit amet, cetero accusamus intellegat at his, usu aeterno erroribus sadip&shy;scing id, nam virtute equidem reprimique ea. Est cu modo oblique theophrastus, vix ex ferri dicam iisque, idque nostrud eam ut. Tation constituto reprimique ut vis. Cu appar&shy;eat dissentias qui.</p>
  </div>
  <div class="signature" role="img" aria-label="Handwritten signature"></div>
  <div class="signatory"><div class="signatory-name">Daniel Hargreave</div><div class="signatory-role">Product Director</div></div>
  <div class="footer-bar">info@harborventurepartners.com.au &nbsp;|&nbsp; www.harborventurepartners.com.au</div>
  <div class="badge badge--seal" role="img" aria-label="DWL membership badge"></div>
  <div class="partner"><span class="partner-dot"></span><span class="partner-name">NTQR</span></div>
</section>

<!-- Envelope with address lines -->
<section class="slip" aria-label="Envelope with address area">
  <div class="brand"><div class="brand-ring"></div><div class="brand-name">Harbor<br>Venture<br>Partners</div></div>
  <div class="stamp-box">STAMP</div>
  <div class="address-lines">
    <span style="top:115px"></span><span style="top:136px"></span><span style="top:158px"></span><span style="top:180px"></span>
  </div>
  <div class="base-band"></div>
</section>

<!-- Envelope back -->
<section class="envelope" aria-label="Envelope back">
  <svg class="flap-line" width="466" height="32" viewBox="0 0 466 32" aria-hidden="true">
    <path d="M2 0 Q6 22 14 30 L452 30 Q460 22 464 0" fill="none" stroke="#ececec" stroke-width="1"/>
  </svg>
  <div class="brand"><div class="brand-ring"></div><div class="brand-name">Harbor<br>Venture<br>Partners</div></div>
  <div class="envelope-contact">
    2190 Marlow Rd NE #14, Ridgefield, AB T4R 2M6<br>
    P: 403 555 0142 F: 403 555 0187 E: info@harborventurepartners.com.au<br>
    www.harborventurepartners.com.au
  </div>
  <div class="powered-by">Powered by<br>Crale Business Sales</div>
  <div class="badge badge--seal" role="img" aria-label="DWL membership badge"></div>
  <div class="partner"><span class="partner-dot"></span><span class="partner-name">NTQR</span></div>
  <div class="base-band"></div>
</section>

</body>
</html>
```